Its a flyer to a course entitled :
Ultrasound Course

Basically we teach students about the use of ultrasound for very sick patients

-I need a title in 3D
-I need an attractive design please
something extraordinary

Please if you have any ongoing project let me know Thanks

Dear Designers Was looking for something new that I did not see before, unfortunately did not find that yet! To clarify the idea, remember the T.V series 'TQ'.. so we have a sick patient like the one you have seen in the series and now we are using Ultrasound to help get the diagnosis and even it helps us in the procedures so basically will use the ultrasound to help saving those patients and give them the treatment in a short time.j

```html
<!DOCTYPE html>
<html lang="en">
<head>
<meta charset="utf-8">
<title>Emergency &amp; Critical Care Ultrasound Course</title>
<link rel="stylesheet" href="https://fonts.googleapis.com/css2?family=Audiowide&display=swap">
<style>
  :root {
    --stage-light: #eeeef0;
    --stage-mid: #c4c4c8;
    --stage-dark: #9c9ca2;
    --panel: #000000;
    --magenta: #e040d8;
    --title-fill: #e6d2ee;
    --title-edge: #7a1f86;
    --figure-blue: #3d7fa3;
    --figure-red: #9a2f36;
    --figure-shadow: #1a2c38;
  }
  * { margin: 0; padding: 0; box-sizing: border-box; }
  html, body {
    width: 1200px;
    height: 750px;
    overflow: hidden;
  }
  body {
    background: linear-gradient(160deg, var(--stage-mid) 0%, var(--stage-light) 30%, var(--stage-mid) 55%, var(--stage-light) 78%, var(--stage-dark) 100%);
  }
  .flyer {
    position: absolute;
    left: 100px;
    top: 140px;
    width: 1000px;
    height: 470px;
    background: var(--panel);
    overflow: hidden;
    box-shadow: 4px 5px 8px rgba(0, 0, 0, 0.55);
  }
  .light-trails {
    position: absolute;
    inset: 0;
    width: 100%;
    height: 100%;
  }
  .anatomy-figure {
    position: absolute;
    left: 28px;
    top: 24px;
    width: 68px;
    height: 116px;
    border-radius: 26px 26px 10px 10px;
    background:
      radial-gradient(ellipse 40% 30% at 52% 35%, var(--figure-red) 0%, rgba(154, 47, 54, 0) 100%),
      linear-gradient(180deg, var(--figure-blue) 0%, var(--figure-shadow) 100%);
    opacity: 0.8;
  }
  .course-title {
    position: absolute;
    left: 0;
    right: 0;
    top: 386px;
    text-align: center;
    font-family: "Audiowide", sans-serif;
    font-size: 33px;
    font-weight: 400;
    line-height: 40px;
    letter-spacing: 0;
    color: var(--title-fill);
    transform: scaleX(0.915);
    transform-origin: 50% 50%;
    text-shadow:
      0 0 2px var(--title-edge),
      1px 1px 0 var(--title-edge),
      2px 2px 0 #4e0f58,
      3px 3px 0 #33083a,
      0 0 10px var(--magenta),
      0 0 18px var(--magenta);
    white-space: nowrap;
  }
</style>
</head>
<body>
  <main class="flyer">
    <svg class="light-trails" viewBox="0 0 1000 470" aria-hidden="true">
      <defs>
        <filter id="soft-glow" x="-20%" y="-50%" width="140%" height="200%">
          <feGaussianBlur stdDeviation="4"/>
        </filter>
        <filter id="wide-haze" x="-20%" y="-50%" width="140%" height="200%">
          <feGaussianBlur stdDeviation="12"/>
        </filter>
        <linearGradient id="trail-pink" x1="0" x2="1" y1="0" y2="0">
          <stop offset="0" stop-color="#e040d8" stop-opacity="0.2"/>
          <stop offset="0.35" stop-color="#e040d8" stop-opacity="1"/>
          <stop offset="0.8" stop-color="#e040d8" stop-opacity="0.7"/>
          <stop offset="1" stop-color="#e040d8" stop-opacity="0"/>
        </linearGradient>
        <linearGradient id="trail-silver" x1="0" x2="1" y1="0" y2="0">
          <stop offset="0" stop-color="#c9c9cc" stop-opacity="0"/>
          <stop offset="0.5" stop-color="#c9c9cc" stop-opacity="0.8"/>
          <stop offset="1" stop-color="#c9c9cc" stop-opacity="0"/>
        </linearGradient>
      </defs>

      <g class="silver-trails" fill="none" stroke="url(#trail-silver)">
        <path d="M180 260 C 400 180, 620 80, 850 0" stroke-width="34" filter="url(#wide-haze)" opacity="0.55"/>
        <path d="M220 240 C 420 160, 600 70, 780 0" stroke-width="4" filter="url(#soft-glow)"/>
        <path d="M260 250 C 460 160, 640 80, 860 10" stroke-width="2" opacity="0.7"/>
        <path d="M320 280 C 520 200, 720 120, 920 60" stroke-width="2" opacity="0.45"/>
        <path d="M380 430 C 600 370, 800 330, 1000 300" stroke-width="22" filter="url(#wide-haze)" opacity="0.5"/>
        <path d="M420 410 C 640 365, 820 330, 1000 310" stroke-width="2" opacity="0.6"/>
        <path d="M600 210 C 760 150, 880 110, 1000 80" stroke-width="2" opacity="0.35"/>
      </g>

      <g class="magenta-trails" fill="none" stroke="url(#trail-pink)" stroke-linecap="round">
        <path d="M80 195 C 260 190, 420 120, 560 30" stroke-width="14" filter="url(#wide-haze)"/>
        <path d="M80 195 C 260 190, 420 120, 560 30" stroke-width="5" filter="url(#soft-glow)"/>
        <path d="M80 195 C 260 190, 420 120, 560 30" stroke="#ffd0fb" stroke-width="1.4" opacity="0.85"/>
        <path d="M0 272 C 240 280, 480 245, 680 185" stroke-width="16" filter="url(#wide-haze)"/>
        <path d="M0 272 C 240 280, 480 245, 680 185" stroke-width="5" filter="url(#soft-glow)"/>
        <path d="M0 272 C 240 280, 480 245, 680 185" stroke="#ffd0fb" stroke-width="1.4" opacity="0.85"/>
        <path d="M150 465 C 380 445, 520 440, 660 438" stroke-width="5" filter="url(#soft-glow)" opacity="0.6"/>
      </g>
    </svg>

    <div class="anatomy-figure" role="img" aria-label="Small translucent anatomical torso illustration showing internal organs"></div>

    <h1 class="course-title">EMERGENCY &amp; CRITICAL CARE ULTRASOUND COURSE</h1>
  </main>
</body>
</html>
```